Natural cosmetics company is looking for a designer to produce the labels of the products and

Hello, Nus need a label and logo design for our brand LW PURELEAF. It is a brand specializing in the sale of 100% Natural cosmetic products on the internet. The first range is based on snail slime. I am looking for a clean design in green tones. The final design must be forwarded to the supplier for printing and shipping of the products. I realized a first idea for a logo, but I am interested in other ideas / suggestions. You have carte blanche :)
Here are the rules to follow for sending labels to the supplier:
• Sizes:
- Airless bottle: 10.3 x 5.5 cm
- Jar: 20x2.5cm
• Files must be in Corel Draw (. cdr) and / or vector PDF format
You must attach the file of the fonts used for the text in the label - We need this file as many fonts are difficult to find and we might need to move some text around for printing purposes
• The logo of your brand must be in a vector format along with all other components.
• Please do not add any borders or any cut marks to the design. We will do it on our end as we need to follow specific indications with our printing suppliers.
• All text and graphics must be at least 6mm from the edge
• The dimensions indicated by us must be respected in the overall size of the label
• The resolution to be used should be 300 cpi and in CMYK
• The text size should be readable and at least 4.5 points.

```html
<!DOCTYPE html>
<html lang="en">
<head>
<meta charset="utf-8">
<title>LW PURELEAF Snail Slime Labels</title>
<link rel="stylesheet" href="https://fonts.googleapis.com/css2?family=Didact+Gothic&display=swap">
<style>
:root{
  --bg:#f4f4f4;
  --label:#ffffff;
  --edge:#d6d6d6;
  --ink:#1a1a1a;
  --green:#6fb52c;
  --green-light:#a6d65a;
}
*{margin:0;padding:0;box-sizing:border-box}
html,body{width:1200px;height:923px;overflow:hidden;background:var(--bg)}
body{position:relative;font-family:"Didact Gothic",sans-serif;color:var(--ink)}
.label{position:absolute;background:var(--label);border:1px solid var(--edge)}
.jar-label{left:54px;top:57px;width:1087px;height:137px}
.bottle-label{left:157px;top:380px;width:880px;height:469px}
.block{position:absolute;text-align:center;line-height:1.23}
.brand-mark{position:absolute;border-radius:50%;border:2px solid var(--ink);display:flex;align-items:center;justify-content:center;text-align:center;line-height:1.1;letter-spacing:.5px;background:var(--label)}
.product-photo{position:absolute;border-radius:50%;background:radial-gradient(circle at 55% 60%,#8a6b3a 0,#6b8a2a 25%,var(--green) 55%,var(--green-light) 100%);box-shadow:0 0 0 3px var(--label),0 0 0 5px var(--green)}
.product-name{position:absolute;text-align:center;letter-spacing:.42em;white-space:nowrap}
.volume{position:absolute;text-align:center;white-space:nowrap}
.heading{display:block}
.badges{position:absolute;display:flex;flex-direction:column;align-items:center}
.badge{border:2px solid var(--ink)}
.vertical{position:absolute;writing-mode:vertical-rl;transform:rotate(180deg);white-space:nowrap;line-height:1.05;text-align:left}
</style>
</head>
<body>

<section class="label jar-label">
  <div class="block" style="left:20px;top:21px;width:272px;font-size:12px;line-height:1.24">LW PURELEAF Eye Effect Day Cream Lorem ipsum dolor sit amet. Dolor dolores kasd sed ipsum elitr amet ut. Et eirmod at stet. Ipsum est gubergren. Quis dolor amet qui sadipscing suscipit dolor. Aliquip wisi vel invidunt accusam augue. Nihil elitr autem. Consectetuer vero elitr. Praesent vero delenit</div>
  <div class="product-photo" role="img" aria-label="Photo of a snail on a green leaf" style="left:359px;top:19px;width:100px;height:100px"></div>
  <div class="brand-mark" style="left:477px;top:21px;width:65px;height:65px;font-size:8px">LW<br>PURELEAF</div>
  <div class="product-name" style="left:459px;top:97px;width:100px;font-size:10px">SNAIL SLIME</div>
  <div class="volume" style="left:459px;top:112px;width:100px;font-size:9.5px">℮30ml/1.01 fl.oz.</div>
  <div class="block" style="left:626px;top:21px;width:196px;font-size:12px;line-height:1.24"><span class="heading">DIRECTIONS:</span>Quis dolor amet qui sadipscing suscipit dolor. Aliquip wisi vel invidunt accusam augue. Nihil elitr autem. Consectetuer vero elitr. Praesent vero delenit sed ex</div>
  <div class="block" style="left:834px;top:21px;width:170px;font-size:12px;line-height:1.24"><span class="heading">INGREDIENTS:</span>Water,Butylene Glycol, Tetrapeptide,Palmitoyl Tripeptide,Collagen Amino Acids,Dexpanthenol,Sodium Hyaluronate,Phenoxyethanol</div>
  <div class="badges" style="left:1016px;top:18px;gap:9px">
    <div class="badge" style="width:14px;height:12px;border-radius:3px"></div>
    <div class="badge" style="width:18px;height:18px;border-radius:50%"></div>
    <div class="badge" style="width:18px;height:18px;border-radius:50%"></div>
    <div class="badge" style="width:18px;height:16px;border-radius:2px"></div>
  </div>
  <div class="vertical" style="left:1042px;top:30px;height:92px;font-size:8.5px">LW Pureleaf,<br>Adress,adress,adress<br>MADE IN CHINA</div>
</section>

<section class="label bottle-label">
  <div class="block" style="left:30px;top:64px;width:132px;font-size:16px;line-height:1.3">LW Pureleaf Snail Slime Lorem ipsum dolor sit amet. Dolor dolores kasd sed ipsum elitr amet ut. Et eirmod at stet. Ipsum est gubergren. Quis dolor amet qui sadipscing suscipit dolor. Aliquip wisi vel invidunt accusam augue. Nihil elitr autem. Consectetuer vero elitr. Praesent vero delenit sed ex</div>
  <div class="brand-mark" style="left:406px;top:26px;width:69px;height:69px;font-size:9px">LW<br>PURELEAF</div>
  <div class="product-photo" role="img" aria-label="Photo of a snail on a green leaf" style="left:356px;top:158px;width:172px;height:172px"></div>
  <div class="product-name" style="left:326px;top:414px;width:230px;font-size:16px">SNAIL SLIME</div>
  <div class="volume" style="left:326px;top:436px;width:230px;font-size:16px">℮30ml/1.01 fl.oz.</div>
  <div class="block" style="left:662px;top:32px;width:150px;font-size:14px;line-height:1.25"><span class="heading">INGREDIENTS:</span>Water,<br>Butylene Glycol,<br>Tetrapeptide,<br>Palmitoyl<br>Tripeptide,<br>Collagen Amino<br>Acids,Dexpanthenol,<br>Sodium<br>Hyaluronate,<br>Phenoxyethanol,<br>Ethylhexylglycerin</div>
  <div class="block" style="left:668px;top:253px;width:136px;font-size:14px;line-height:1.25"><span class="heading">DIRECTIONS:</span>Quis dolor amet qui sadipscing suscipit dolor. Aliquip wisi vel invidunt accusam augue. Nihil elitr autem. Consectetuer vero elitr. Praesent vero delenit sed ex</div>
  <div class="badges" style="left:816px;top:34px;gap:18px">
    <div class="badge" style="width:20px;height:18px;border-radius:4px"></div>
    <div class="badge" style="width:30px;height:30px;border-radius:50%"></div>
    <div class="badge" style="width:30px;height:30px;border-radius:50%"></div>
    <div class="badge" style="width:28px;height:26px;border-radius:3px"></div>
  </div>
  <div class="vertical" style="left:803px;top:250px;height:190px;font-size:14px">LW Pureleaf,<br>Adress,adress,adress<br>MADE IN FRANCE</div>
</section>

</body>
</html>
```